Brightwave Learners Agency business cards

Australian company about to start offering its services. We recruit international students to come to study English, vocational education and postgraduate courses in Australia. We help them find the institution and select the right city they want to come to Australia. We are a young, online oriented and supportive agency. Our clients are between 18 and 35 years old, mainly University students, young professionals or people with work experience. We provide much more information that any other agency offer. We administrate a Facebook group with more than 11.000 members that daily ask questions about general information when coming to Australia, while they are here and even after they leave the country

Target Market(s)

International students from South America, Central America and Europe

Industry/Entity Type

Student

Contact Information for Business Card

Tomas Velorin
Managing Director
tomas@kelvona.com.au
www.kelvrona.com.au
+61 497285064
Melbourne, Australia

Font styles to use
Serif
Sans Serif

Colors

Designer to choose colors to be used in the design.

Requirements
Must have
• Horizontal design
• Standard business card size and shape. If font uses green or yellow colours, they will have to match the ones from the logo
Nice to have
• UPDATE: Use the contents of the green image to design one of the card sides. Use our logo in the background of that side as watermark.
• Passport image, or immigration stamps. A picture of the Yarra River (from Melbourne) would be cool as well.
Should not have
• Non-standard business card size and shape
• Not black as the background colour of any sides as we are not a VIP agency or a hight class service. We are orientes to young people and they like colours, pictures, something attractive.
• Vertical design
• NO YELLOW or BLACK AS THE BACKGROUND COLOUR OF ANY SIDE OF THE BIZ CARD

```html
<!DOCTYPE html>
<html lang="en">
<head>
<meta charset="utf-8">
<title>Brightwave Learners Agency – Business Cards</title>
<link rel="stylesheet" href="https://fonts.googleapis.com/css2?family=Lato:ital,wght@0,400;0,700;1,400&display=swap">
<style>
  :root {
    --backdrop: #161616;
    --paper: #fbf8f2;
    --green: #146143;
    --yellow: #e3bd22;
    --ink: #2a2a2a;
    --white: #ffffff;
  }
  * { box-sizing: border-box; margin: 0; padding: 0; }
  html, body {
    width: 1200px; height: 1000px; overflow: hidden;
    background: var(--backdrop);
    font-family: "Lato", Arial, sans-serif;
  }
  .stage {
    position: relative; width: 1200px; height: 1000px;
  }
  .card {
    position: absolute;
    width: 500px; height: 286px;
    background: var(--paper);
    box-shadow: 0 6px 18px rgba(0,0,0,.45);
  }
  .card--front { left: 70px; top: 357px; }
  .card--back  { left: 630px; top: 357px; }

  /* Front */
  .front-panel {
    position: absolute; left: 16px; top: 16px; right: 16px; bottom: 34px;
    background: var(--green);
  }
  .brand {
    position: absolute; display: flex; align-items: center; gap: 10px;
    font-weight: 700; font-size: 38px; letter-spacing: .5px;
  }
  .brand__dot {
    width: 14px; height: 14px; border-radius: 50%;
  }
  .front-panel .brand { left: 40px; top: 62px; color: var(--white); }
  .front-panel .brand__dot { background: var(--white); }
  .tagline {
    position: absolute; right: 28px; bottom: 26px;
    color: var(--white); font-size: 16px;
  }

  /* Back */
  .name-band {
    position: absolute; left: 16px; right: 16px; top: 16px; height: 64px;
    background: var(--yellow);
    display: flex; align-items: center; justify-content: center;
  }
  .name-band__name {
    color: var(--ink); font-size: 21px; font-weight: 400; letter-spacing: .5px;
    text-transform: uppercase;
  }
  .card--back .brand { left: 30px; top: 150px; color: var(--green); font-size: 32px; }
  .card--back .brand__dot { background: var(--green); width: 12px; height: 12px; }
  .contact {
    position: absolute; left: 290px; top: 112px;
    color: var(--ink); font-size: 14px; line-height: 1;
    list-style: none;
  }
  .contact__role { font-style: italic; margin-bottom: 10px; }
  .contact__item {
    display: flex; align-items: center; gap: 9px; margin-bottom: 9px;
  }
  .contact__item svg { width: 13px; height: 13px; flex: none; fill: var(--ink); }
  .contact__city { font-size: 15px; margin-top: 2px; }
</style>
</head>
<body>
<main class="stage">

  <section class="card card--front" aria-label="Business card front">
    <div class="front-panel">
      <div class="brand"><span class="brand__dot"></span>Brightwave</div>
      <p class="tagline">Hacemos más por ti!</p>
    </div>
  </section>

  <section class="card card--back" aria-label="Business card back">
    <div class="name-band"><h1 class="name-band__name">Tomas Velorin</h1></div>
    <div class="brand"><span class="brand__dot"></span>Brightwave</div>
    <ul class="contact">
      <li class="contact__role">Managing director</li>
      <li class="contact__item">
        <svg viewBox="0 0 24 24" aria-hidden="true"><path d="M6.6 10.8a15.1 15.1 0 0 0 6.6 6.6l2.2-2.2c.3-.3.7-.4 1-.2 1.1.4 2.3.6 3.6.6.6 0 1 .4 1 1V20c0 .6-.4 1-1 1A17 17 0 0 1 3 4c0-.6.4-1 1-1h3.5c.6 0 1 .4 1 1 0 1.3.2 2.5.6 3.6.1.3 0 .7-.2 1z"/></svg>
        +61 49 72 85 064
      </li>
      <li class="contact__item">
        <svg viewBox="0 0 24 24" aria-hidden="true"><path d="M2 5h20v14H2zm2 2v.5l8 5 8-5V7l-8 5z"/></svg>
        tomas@kelvona.com.au
      </li>
      <li class="contact__item">
        <svg viewBox="0 0 24 24" aria-hidden="true"><path d="M12 2a10 10 0 1 0 0 20 10 10 0 0 0 0-20zm6.9 6h-3a15.7 15.7 0 0 0-1.3-3.9A8 8 0 0 1 18.9 8zM12 4c.8 1.2 1.5 2.5 1.9 4h-3.8c.4-1.5 1.1-2.8 1.9-4zM4.3 14a8 8 0 0 1 0-4h3.4a16.5 16.5 0 0 0 0 4zm.8 2h3c.3 1.4.8 2.7 1.3 3.9A8 8 0 0 1 5.1 16zm3-8h-3a8 8 0 0 1 4.3-3.9C8.9 5.3 8.4 6.6 8.1 8zM12 20c-.8-1.2-1.5-2.5-1.9-4h3.8c-.4 1.5-1.1 2.8-1.9 4zm2.3-6H9.7a14.7 14.7 0 0 1 0-4h4.6a14.7 14.7 0 0 1 0 4zm.3 5.9c.5-1.2 1-2.5 1.3-3.9h3a8 8 0 0 1-4.3 3.9zm1.7-5.9a16.5 16.5 0 0 0 0-4h3.4a8 8 0 0 1 0 4z"/></svg>
        www.kelvrona.com.au
      </li>
      <li class="contact__city">Melbourne, Australia</li>
    </ul>
  </section>

</main>
</body>
</html>
```